Expanding Training Company needs a powerpoint template to deliver a consistent professional image

We want to start with a ppt template that is clean and flexible.
We are a small training organisation focusing on personal effectiveness, leadership, management and change. The MD is a New Zealander living in the United Kingdom and loves the idea of the clean green image that NZ has and wants the PowerPoint template to reflect that. We are pragmatic in what we do - everything comes back to performance improvement. Our clients are big players and our presentations need to be as clean, and as professional as theirs. We need a template that is versatile and can have their logos added as necessary.
Our training tends to be very current and as such we would like to use a lot of images and less words/bullets. We have company colours, logos and fonts that we are happy with and will continue to use.

Here are our company values to give you a sense of what we are about…

As a learning organisation we are always looking to continually improve and renew, our material, ideas, and methods, and are continually on the look out for new techniques, interventions and applications that provide measurable results to our clients.

We think life is about people and relationships, and we are prepared to walk away if people don't keep their word, are untrustworthy or lack integrity, as life is just too short to work with arses.
And because we are not arses we admit when we are wrong and make good on our commitments.

For our clients its all about performance and training is a performance enhancer, we aim to provide training excellence tin all its guises that delivers performance and happy clients.

We harness the value of the team, we believe in Interdependence.

We make life easier for our clients and each other.

Flexibility, innovation and future focus/vision are what our clients can count on us for.

Work is one of many of life's great facilitators, we recognise and value the others - its not just about work.

Industry/Entity Type

It Company

Other font styles liked:
• Avenir Next

Colors
abd037
9bcb3c

Requirements
Must have
• A clean look with multiple options for inserting images, tables, videos, text boxes etc
• copyright information
Nice to have
• Slide masters

```html
<!DOCTYPE html>
<html lang="en">
<head>
<meta charset="utf-8">
<title>Fernway Consulting – Presentation Template</title>
<link rel="stylesheet" href="https://fonts.googleapis.com/css2?family=Oswald:wght@500;600&family=Open+Sans:wght@400;600;700&display=swap">
<style>
:root{
  --green:#1b8f3f;
  --green-dark:#127a33;
  --lime:#8cc63f;
  --mint:#e3f3e6;
  --cream:#eef3e4;
  --sky:#e6edf6;
  --orange:#e57c1e;
  --ink:#444;
  --stage:#c7c7c7;
  --white:#fff;
}
*{box-sizing:border-box;margin:0;padding:0}
html,body{width:854px;height:1200px;overflow:hidden}
body{background:var(--stage);font-family:"Open Sans",Arial,sans-serif;color:var(--ink);position:relative}
.slide{position:absolute;width:325px;height:244px;background:var(--white);overflow:hidden;box-shadow:2px 3px 6px rgba(0,0,0,.35)}
.col-l{left:88px}.col-r{left:448px}
.row-1{top:58px}.row-2{top:337px}.row-3{top:615px}.row-4{top:897px}
.abs{position:absolute}
.head{font-family:"Oswald",Arial,sans-serif;font-weight:600;color:var(--green);text-transform:uppercase;letter-spacing:-.2px;line-height:1.1}
.photo{position:absolute}
.tiny{font-size:4.6px;line-height:1.45;color:#666}
.small{font-size:6.4px;line-height:1.45;color:#555}
.brand{display:flex;align-items:center;gap:3px;font-family:"Open Sans",Arial,sans-serif;color:#444;font-weight:400}
.brand .dot{width:10px;height:10px;border-radius:50%;background:#444}
.footline{position:absolute;left:40px;right:0;bottom:14px;height:1px;background:#555}
.icon{display:block;margin:0 auto}
</style>
</head>
<body>

<!-- Cover -->
<section class="slide col-l row-1">
  <div class="photo" style="left:0;top:0;width:120px;height:244px;background:linear-gradient(160deg,#9aa6b2,#5d6a78 55%,#c9cfd4)" role="img" aria-label="Business colleagues talking in an office"></div>
  <div class="photo" style="left:238px;top:0;width:87px;height:244px;background:linear-gradient(200deg,#d8dee3,#6a7581 45%,#3d4651)" role="img" aria-label="Smiling businessmen in suits"></div>
  <div class="brand abs" style="left:136px;top:112px;font-size:14px;font-weight:600;color:var(--green)"><span class="dot" style="background:var(--green);width:14px;height:14px"></span>Fernway</div>
</section>

<!-- Our services -->
<section class="slide col-r row-1">
  <h2 class="head abs" style="left:0;right:0;top:23px;text-align:center;font-size:17px">Our Services</h2>
  <div class="abs" style="left:24px;top:71px;width:136px;height:142px;background:var(--cream);border-bottom:2px solid var(--green)">
    <div style="background:var(--green);color:#fff;font-size:6px;font-weight:700;text-align:center;height:20px;line-height:20px">LOREM IPSUM</div>
    <p class="small" style="text-align:center;padding:12px 12px 0">Lorem ipsum dolor sit amet consectetur adipiscing elit. Cras bibendum mattis leo, ac efficitur ipsum lobortis non. Praesent vitae pulvinar metus. Phasellus accumsan elementum condimentum. Nullam rutrum, tellus tincidunt scelerisque elementum</p>
  </div>
  <div class="abs" style="left:171px;top:71px;width:135px;height:142px;background:var(--mint);border-bottom:2px solid var(--lime)">
    <div style="background:var(--lime);color:#fff;font-size:6px;font-weight:700;text-align:center;height:20px;line-height:20px">LOREM IPSUM</div>
    <p class="small" style="text-align:center;padding:12px 12px 0">Lorem ipsum dolor sit amet consectetur adipiscing elit. Cras bibendum mattis leo, ac efficitur ipsum lobortis non. Praesent vitae pulvinar metus. Phasellus accumsan elementum condimentum. Nullam rutrum, tellus tincidunt scelerisque elementum</p>
  </div>
  <div class="footline"></div>
  <div class="brand abs" style="left:12px;bottom:9px;font-size:7px"><span class="dot"></span>Fernway</div>
</section>

<!-- Green intro with icon card -->
<section class="slide col-l row-2" style="background:var(--green)">
  <div class="photo" style="left:180px;top:0;width:145px;height:244px;background:linear-gradient(180deg,#b9c6c9,#7f8f8c 60%,#5a6a60)" role="img" aria-label="Bright office corridor"></div>
  <div class="abs" style="left:0;top:0;width:190px;height:244px;background:var(--green);opacity:.95"></div>
  <p class="abs" style="left:20px;top:46px;width:94px;color:#fff;font-size:7.8px;line-height:1.38;text-align:center"><b>Lorem ipsum dolor sit amet consectetur adipiscing elit. Cras bibendum mattis leo, ac efficitur ipsum lobortis non. Praesent vitae pulvinar</b> Lorem ipsum dolor sit amet consectetur adipiscing elit. Cras bibendum mattis leo, ac efficitur ipsum lobortis non. Praesent vitae pulvinar</p>
  <div class="abs" style="left:127px;top:16px;width:159px;height:211px;background:#fff;padding:18px 12px 0;text-align:center">
    <svg class="icon" width="22" height="18" viewBox="0 0 22 18"><rect x="1" y="4" width="20" height="13" rx="1.5" fill="var(--green)"/><rect x="7" y="1" width="8" height="4" fill="none" stroke="var(--green)" stroke-width="2"/><rect x="1" y="9" width="20" height="1.5" fill="#fff"/></svg>
    <p class="tiny" style="margin:6px 0 18px">Lorem ipsum dolor sit amet consectetur adipiscing elit. Cras bibendum mattis leo, ac efficitur ipsum lobortis non. Praesent vitae pulvinar metus. Phasellus accumsan elementum condimentum. Nullam rutrum, tellus</p>
    <svg class="icon" width="22" height="18" viewBox="0 0 22 18"><rect x="1" y="1" width="20" height="16" rx="1" fill="none" stroke="var(--green)" stroke-width="2"/><rect x="1" y="1" width="20" height="4" fill="var(--green)"/><g fill="var(--green)"><rect x="4" y="8" width="2" height="2"/><rect x="8" y="8" width="10" height="2"/><rect x="4" y="12" width="2" height="2"/><rect x="8" y="12" width="10" height="2"/></g></svg>
    <p class="tiny" style="margin:6px 0 18px">Lorem ipsum dolor sit amet consectetur adipiscing elit. Cras bibendum mattis leo, ac efficitur ipsum lobortis non. Praesent vitae pulvinar metus. Phasellus accumsan elementum condimentum. Nullam rutrum, tellus</p>
    <svg class="icon" width="24" height="20" viewBox="0 0 24 20"><circle cx="9" cy="11" r="6" fill="none" stroke="var(--green)" stroke-width="4" stroke-dasharray="3 2"/><circle cx="9" cy="11" r="2" fill="var(--green)"/><circle cx="18" cy="5" r="3.5" fill="none" stroke="var(--green)" stroke-width="2.5" stroke-dasharray="2 1.5"/></svg>
    <p class="tiny" style="margin-top:6px">Lorem ipsum dolor sit amet consectetur adipiscing elit. Cras bibendum mattis leo, ac efficitur ipsum lobortis non. Praesent vitae pulvinar metus. Phasellus accumsan elementum condimentum. Nullam rutrum, tellus</p>
  </div>
</section>

<!-- Photo with text -->
<section class="slide col-r row-2">
  <div class="abs" style="left:0;top:190px;width:325px;height:54px;background:var(--green)"></div>
  <div class="photo" style="left:19px;top:35px;width:119px;height:179px;background:linear-gradient(160deg,#dfe3e6,#8e99a3 50%,#2f3a48)" role="img" aria-label="Row of smiling business people"></div>
  <h2 class="head abs" style="left:155px;top:29px;font-size:15px">Lorem ipsum dolor sit</h2>
  <p class="abs" style="left:155px;top:52px;font-size:6.2px;font-weight:700;color:var(--orange)">LOREM IPSUM DOLOR</p>
  <ul class="abs small" style="left:162px;top:70px;font-size:5.2px;list-style:disc">
    <li>Lorem ipsum dolor sit amet</li><li>consectetur adipiscing elit</li><li>Cras bibendum mattis leo, ac</li><li>efficitur ipsum lobortis non</li>
  </ul>
  <p class="abs" style="left:155px;top:111px;font-size:5.2px;font-weight:700;color:var(--orange)">Lorem ipsum dolor:</p>
  <p class="abs tiny" style="left:155px;top:123px;width:155px;font-size:5px">Lorem ipsum dolor sit amet consectetur adipiscing elit. Cras bibendum mattis leo, ac efficitur ipsum lobortis non. Praesent vitae pulvinar metus. Phasellus accumsan elementum condimentum. Nullam rutrum, tellus tincidunt scelerisque placerat, justo lectus luctus odio, varius auctor urna lacus sed nisl. Suspendisse at placerat sem. Duis tincidunt augue vel eros hendrerit tempus.</p>
  <p class="head abs" style="left:170px;top:206px;color:#fff;font-size:11px">Lorem ipsum dolor sit</p>
</section>

<!-- Team -->
<section class="slide col-l row-3">
  <div class="abs" style="left:0;top:125px;width:325px;height:119px;background:var(--green)"></div>
  <h2 class="head abs" style="left:0;right:0;top:24px;text-align:center;font-size:17px">Out Team Members</h2>
  <div class="photo" style="left:37px;top:84px;width:76px;height:76px;border-radius:50%;border:2px solid var(--lime);background:radial-gradient(circle,#c9b7c9,#6f5f8a)" role="img" aria-label="Portrait of a team member"></div>
  <div class="photo" style="left:124px;top:84px;width:76px;height:76px;border-radius:50%;border:2px solid var(--lime);background:radial-gradient(circle,#c7b7ad,#5d6670)" role="img" aria-label="Portrait of a team member"></div>
  <div class="photo" style="left:211px;top:84px;width:76px;height:76px;border-radius:50%;border:2px solid var(--lime);background:radial-gradient(circle,#8a7f76,#2c2c2c)" role="img" aria-label="Portrait of a team member"></div>
  <div class="abs" style="left:37px;top:166px;width:76px;text-align:center;color:#fff"><p class="head" style="color:#fff;font-size:8.5px">Lorem ipsum</p><p style="font-size:5px">LOREM IPSUM</p></div>
  <div class="abs" style="left:124px;top:166px;width:76px;text-align:center;color:#fff"><p class="head" style="color:#fff;font-size:8.5px">Lorem ipsum</p><p style="font-size:5px">LOREM IPSUM</p></div>
  <div class="abs" style="left:211px;top:166px;width:76px;text-align:center;color:#fff"><p class="head" style="color:#fff;font-size:8.5px">Lorem ipsum</p><p style="font-size:5px">LOREM IPSUM</p></div>
</section>

<!-- Quality -->
<section class="slide col-r row-3" style="background:linear-gradient(135deg,#1c9b5e,#117a48 50%,#1f8f6a)">
  <h2 class="head abs" style="left:0;right:0;top:26px;text-align:center;color:#fff;font-size:11.5px">Lorem ipsum dolor sit amet consectetur</h2>
  <div class="abs" style="left:36px;top:58px;width:256px;height:164px;background:#fff">
    <div class="photo" style="left:0;top:0;width:128px;height:164px;background:linear-gradient(170deg,#e8ecef,#9aa3ad 55%,#37404c)" role="img" aria-label="Colleagues gathered around a laptop"></div>
    <h3 class="head abs" style="left:140px;top:20px;width:100px;text-align:center;font-size:11px">Quality</h3>
    <ul class="abs tiny" style="left:155px;top:50px;width:96px;font-size:5px;list-style:disc">
      <li>Lorem ipsum dolor sit amet consectetur adipiscing elit. Cras</li>
      <li>Lorem ipsum dolor sit amet consectetur adipiscing elit. Cras</li>
      <li>Lorem ipsum dolor sit amet consectetur adipiscing elit. Cras</li>
      <li>Lorem ipsum dolor sit amet consectetur adipiscing elit. Cras</li>
      <li>Lorem ipsum dolor sit amet consectetur adipiscing elit. Cras</li>
      <li>Lorem ipsum dolor sit amet consectetur adipiscing elit. Cras</li>
    </ul>
  </div>
</section>

<!-- Three columns -->
<section class="slide col-l row-4" style="background:var(--green)">
  <div class="photo" style="left:0;top:150px;width:325px;height:94px;background:linear-gradient(180deg,#c8c2b6,#8a7f70)" role="img" aria-label="Office hallway with people walking"></div>
  <h2 class="head abs" style="left:0;right:0;top:29px;text-align:center;color:#fff;font-size:14px;font-weight:500;line-height:1.45">Lorem ipsum dolor sit amet<br>consectetur adipiscing elit.</h2>
  <div class="abs" style="left:33px;top:95px;width:259px;height:149px;background:#fff;display:flex;justify-content:space-around;padding:16px 10px 0">
    <div style="width:68px;text-align:center">
      <svg class="icon" width="22" height="22" viewBox="0 0 22 22"><rect x="1" y="2" width="20" height="11" rx="2" fill="var(--green)"/><circle cx="8" cy="15" r="4" fill="var(--green)"/><circle cx="14" cy="15" r="4" fill="var(--green)"/><rect x="5" y="17" width="12" height="4" fill="var(--green)"/></svg>
      <p style="font-size:5.5px;font-weight:700;color:var(--green);margin:8px 0 4px">LOREM IPSUM</p>
      <p class="tiny" style="color:#333;font-weight:600">Lorem ipsum dolor sit amet consectetur adipiscing elit. Cras bibendum mattis leo, ac efficitur ipsum lobortis non. Praesent vitae pulvinar metus. Phasellus accumsan elementum condimentum. Nullam rutrum, tellus tincidunt scelerisque elementum</p>
    </div>
    <div style="width:68px;text-align:center">
      <svg class="icon" width="24" height="22" viewBox="0 0 24 22"><path d="M12 1 23 6H1Z" fill="var(--green)"/><rect x="2" y="7" width="20" height="2" fill="var(--green)"/><g fill="var(--green)"><rect x="4" y="10" width="2.5" height="8"/><rect x="9" y="10" width="2.5" height="8"/><rect x="13" y="10" width="2.5" height="8"/><rect x="17.5" y="10" width="2.5" height="8"/></g><rect x="1" y="19" width="22" height="2.5" fill="var(--green)"/></svg>
      <p style="font-size:5.5px;font-weight:700;color:var(--green);margin:8px 0 4px">LOREM IPSUM</p>
      <p class="tiny" style="color:#333;font-weight:600">Lorem ipsum dolor sit amet consectetur adipiscing elit. Cras bibendum mattis leo, ac efficitur ipsum lobortis non. Praesent vitae pulvinar metus. Phasellus accumsan elementum condimentum. Nullam rutrum, tellus tincidunt scelerisque elementum</p>
    </div>
    <div style="width:68px;text-align:center">
      <svg class="icon" width="26" height="22" viewBox="0 0 26 22"><path d="M1 4h8l2 3h10v3H6L1 20Z" fill="var(--green)"/><path d="M6 10h19l-5 10H1Z" fill="var(--green)"/></svg>
      <p style="font-size:5.5px;font-weight:700;color:var(--green);margin:8px 0 4px">LOREM IPSUM</p>
      <p class="tiny" style="color:#333;font-weight:600">Lorem ipsum dolor sit amet consectetur adipiscing elit. Cras bibendum mattis leo, ac efficitur ipsum lobortis non. Praesent vitae pulvinar metus. Phasellus accumsan elementum condimentum. Nullam</p>
    </div>
  </div>
</section>

<!-- Numbered list -->
<section class="slide col-r row-4">
  <h2 class="head abs" style="left:0;right:0;top:29px;text-align:center;font-size:17px;font-weight:500">Lorem ipsum dolor sit amet</h2>
  <p class="head abs" style="left:0;right:0;top:55px;text-align:center;font-size:6.5px;font-weight:500">Consectetur adipiscing elit. Cras</p>
  <div class="abs" style="left:23px;top:78px;width:154px">
    <div style="display:flex;height:29px;margin-bottom:4px"><span style="width:26px;background:var(--green);color:#fff;font-weight:700;font-size:8px;display:flex;align-items:center;justify-content:center">01</span><div style="flex:1;background:var(--cream);padding:4px 4px"><p style="font-size:5px;font-weight:700;color:#444">Lorem ipsum dolor sit amet</p><p class="tiny" style="font-size:3.8px">Lorem ipsum dolor sit amet consectetur adipiscing elit. Cras bibendum mattis leo, Lorem ipsum dolor sit amet co</p></div></div>
    <div style="display:flex;height:29px;margin-bottom:4px"><span style="width:26px;background:var(--lime);color:#fff;font-weight:700;font-size:8px;display:flex;align-items:center;justify-content:center">02</span><div style="flex:1;background:var(--sky);padding:4px 4px"><p style="font-size:5px;font-weight:700;color:#444">Lorem ipsum dolor sit amet</p><p class="tiny" style="font-size:3.8px">Lorem ipsum dolor sit amet consectetur adipiscing elit. Cras bibendum mattis leo, Lorem ipsum dolor sit amet co</p></div></div>
    <div style="display:flex;height:29px;margin-bottom:4px"><span style="width:26px;background:var(--green);color:#fff;font-weight:700;font-size:8px;display:flex;align-items:center;justify-content:center">03</span><div style="flex:1;background:var(--cream);padding:4px 4px"><p style="font-size:5px;font-weight:700;color:#444">Lorem ipsum dolor sit amet</p><p class="tiny" style="font-size:3.8px">Lorem ipsum dolor sit amet consectetur adipiscing elit. Cras bibendum mattis leo, Lorem ipsum dolor sit amet co</p></div></div>
    <div style="display:flex;height:29px"><span style="width:26px;background:var(--lime);color:#fff;font-weight:700;font-size:8px;display:flex;align-items:center;justify-content:center">04</span><div style="flex:1;background:var(--sky);padding:4px 4px"><p style="font-size:5px;font-weight:700;color:#444">Lorem ipsum dolor sit amet</p><p class="tiny" style="font-size:3.8px">Lorem ipsum dolor sit amet consectetur adipiscing elit. Cras bibendum mattis leo, Lorem ipsum dolor sit amet co</p></div></div>
  </div>
  <div class="photo" style="left:185px;top:78px;width:123px;height:129px;background:linear-gradient(150deg,#dfe8f1,#8fa6bd 55%,#e9eef3)" role="img" aria-label="Hands using a tablet over printed charts"></div>
  <div class="footline"></div>
  <div class="brand abs" style="left:12px;bottom:9px;font-size:7px"><span class="dot"></span>Fernway</div>
</section>

</body>
</html>
```